Professional Website for Brightfold Laundry Company

Brightfold Laundry Company is a family-owned laundry service provider that has been serving Midtown Atlanta for over 45 years. We provide express clothing and linen washing services to residential and commercial clients in Atlanta and surrounding areas.

The final website and logo design should convey professionalism and give the customer a sense of security in having their personal items laundered with us.

Target Market(s)

Commercial Businesses and high net worth personal customers

Industry/Entity Type

Professional Laundry Services

Coding

Coded - Design and coding required

Number of Pages Required

5+ page

Font styles to use
Sans Serif

Colors
0054AA
0677BA
7BADD7
CADEEF
E8F1F8

Requirements
Must have
• I would like to have the following elements on my website: 1. Blog page 2. Contact Us Form 3. Sign up for service (sample attached) 4. Sections outlined in the content copy page 5. Links to social media accounts.
Nice to have
• A great example is https://www.quillmarsh.example/laundry-pick-up-and-delivery/?utm_term=pick%20up%20and%20delivery%20laundry%20service&utm_campaign=*QM%20United%20States%20%7C%20Search%20(Broad%20KWs)&utm_source=zorvik&utm_medium=ppc&hsa_acc=1111111111&hsa_cam=22222222222&hsa_grp=3333333333333333&hsa_ad=&hsa_src=o&hsa_tgt=kwd-44444444444444:loc-100&hsa_kw=pick%20up%20and%20delivery%20laundry%20service&hsa_mt=e&hsa_net=zorvik&hsa_ver=3&msclkid=00000000000000000000000000000000

```html
<!DOCTYPE html>
<html lang="en">
<head>
<meta charset="utf-8">
<title>Brightfold Laundry Company – Website Pages</title>
<link href="https://fonts.googleapis.com/css2?family=Nunito:wght@400;600;700;800&family=Anton&display=swap" rel="stylesheet">
<style>
:root{
  --navy:#26437a;
  --blue:#0677BA;
  --deep:#0054AA;
  --sky:#7BADD7;
  --ice:#CADEEF;
  --mist:#E8F1F8;
  --band:#8ccae3;
  --yellow:#f6d54b;
  --ink:#2b2f3a;
  --grey:#7a808c;
  --line:#dfe3ea;
  --board:#e4e4e4;
}
*{margin:0;padding:0;box-sizing:border-box}
html,body{width:1200px;height:2286px;overflow:hidden;background:var(--board)}
body{font-family:'Nunito',sans-serif;color:var(--ink)}
.board{position:absolute;left:0;top:0;width:1252px;height:2386px;transform:scale(.9585);transform-origin:0 0;background:var(--board)}
.page{position:absolute;background:#fff;overflow:hidden}
.a{position:absolute}
.page-label{position:absolute;font-family:'Anton',sans-serif;font-size:31px;color:#3a3a3a;letter-spacing:.3px}

.logo{display:flex;align-items:center;gap:3px;font-size:7px;font-weight:800;color:var(--navy)}
.logo-dot{width:6px;height:6px;border-radius:50%;background:var(--sky)}
.nav{display:flex;gap:10px;font-size:5.2px;color:var(--blue)}
.nav .on{color:var(--navy);font-weight:700}
.social{display:flex;gap:5px}
.social i{display:block;width:6px;height:6px;border-radius:50%;border:1.2px solid var(--navy)}
.btn-navy{background:var(--navy);color:#fff;font-size:5px;font-weight:700;display:flex;align-items:center;justify-content:center;border-radius:1px}
.btn-yellow{background:var(--yellow);color:var(--navy);font-size:5px;font-weight:700;display:flex;align-items:center;justify-content:center;border-radius:1px}

.photo{border-radius:1px}
.h-blue{color:var(--blue);font-weight:600}
.tiny{font-size:3.6px;line-height:5.6px;color:var(--grey)}
.center{text-align:center}

.hero-home{background:linear-gradient(180deg,#fff 0%,#f6f9fb 100%)}
.hero-title{font-size:15.5px;line-height:19px;color:var(--blue);font-weight:600;white-space:nowrap}
.feature-band{background:var(--yellow);display:flex;align-items:center;justify-content:space-around;padding:0 18px}
.feature{display:flex;align-items:center;gap:6px;font-size:4.6px;font-weight:800;color:var(--navy)}
.feature i{display:block;width:22px;height:22px;border-radius:50%;border:1.2px solid var(--navy);position:relative}
.feature i::after{content:"";position:absolute;inset:4px;border-radius:50%;border:1px solid var(--navy)}

.service-zone{background:linear-gradient(180deg,var(--band) 0%,#b5dced 45%,var(--mist) 80%,#fff 100%)}
.svc-card{background:#fff;border-radius:4px;box-shadow:0 2px 6px rgba(6,119,186,.12);display:flex;flex-direction:column;align-items:center;padding-top:10px;width:59px;height:66px}
.svc-card svg{width:20px;height:20px}
.svc-name{font-size:4.4px;line-height:5px;text-align:center;margin-top:5px;color:var(--ink)}
.svc-more{font-size:3.8px;color:var(--blue);margin-top:3px}

.setup-zone{background:linear-gradient(180deg,var(--mist),#d5e8f4)}
.step{background:#fff;border-radius:3px;box-shadow:0 2px 6px rgba(0,0,0,.06);width:85px;height:100px;padding:16px 7px 0;text-align:center}
.step-num{position:absolute;width:16px;height:16px;border-radius:50%;background:var(--yellow);font-size:6px;font-weight:800;color:var(--navy);display:flex;align-items:center;justify-content:center}
.step h4{font-size:7px;line-height:8px;color:var(--blue);font-weight:600;margin-bottom:4px}
.step p{font-size:3.6px;line-height:5.2px;color:var(--ink)}

.why-title{font-size:6px;font-weight:700;color:var(--navy);margin-bottom:7px}
.why-text{width:175px}

.cta-title{font-size:13px;line-height:16px;color:var(--navy);font-weight:700;text-align:center}

.faq{width:172px}
.faq-item{border-bottom:1px solid var(--line);font-size:5.3px;color:var(--ink);padding:6px 0}
.faq-open{font-size:3.6px;line-height:5.2px;color:var(--ink);padding:6px 0 8px;border-bottom:1px solid var(--line)}
.chev{position:absolute;width:5px;height:5px;border-right:1px solid var(--ink);border-bottom:1px solid var(--ink);transform:rotate(45deg)}

.footer{position:absolute;left:0;right:0;bottom:0;background:var(--navy);color:#fff}
.f-col{position:absolute}
.f-col h5{font-size:6px;font-weight:400;margin-bottom:7px}
.f-col li{list-style:none;font-size:3.8px;line-height:9px}
.f-phone{display:flex;align-items:center;gap:5px;font-size:6px;margin-bottom:6px}
.f-small{font-size:3.8px;line-height:5px}
.f-social{display:flex;gap:4px;margin:12px 0 8px}
.f-social i{display:block;width:5px;height:5px;border-radius:50%;border:1px solid #fff}

.detail-hero{background:linear-gradient(180deg,var(--band) 0%,#b7dded 55%,var(--mist) 100%)}
.launder-list li{list-style:none;font-size:4.4px;line-height:10.5px;display:flex;align-items:center;gap:4px}
.launder-list li::before{content:"";width:4px;height:4px;border:1px solid var(--blue);border-radius:50%}

.stepper-dot{position:absolute;width:13px;height:13px;border-radius:50%;background:var(--ice);color:#fff;font-size:5px;display:flex;align-items:center;justify-content:center}
.stepper-dot.on{background:var(--sky)}
.select-box{border:1px solid var(--line);background:#f8f7f7}
.select-field{height:16px;border-bottom:1px solid var(--line);font-size:5px;color:#b0b4bc;padding:5px 5px;background:#fff;position:relative}
.select-opt{font-size:5.5px;color:var(--ink);padding:4px 12px 1px}
</style>
</head>
<body>
<div class="board">

<!-- ================= HOME ================= -->
<section class="page" style="left:92px;top:59px;width:481px;height:2266px">

  <div class="a hero-home" style="left:0;top:0;width:481px;height:236px"></div>
  <div class="a photo" role="img" aria-label="Smiling woman in white shirt holding a laundry basket, bright window behind" style="left:236px;top:36px;width:245px;height:200px;background:linear-gradient(90deg,rgba(246,249,251,0) 0%,#efe9e2 30%,#e6ddd2 60%,#d9cfc4 100%)"></div>

  <div class="a logo" style="left:58px;top:14px"><span class="logo-dot"></span>Brightfold Laundry</div>
  <nav class="a nav" style="left:182px;top:17px"><span class="on">Home</span><span>Services</span><span>Contact</span><span>Blog</span></nav>
  <div class="a social" style="left:347px;top:17px"><i></i><i></i></div>
  <div class="a btn-navy" style="left:377px;top:14px;width:46px;height:13px">Sign Up today!</div>

  <h1 class="a hero-title" style="left:58px;top:73px">Professional<br>Laundry Service<br>in Mindtown, Atlanta</h1>
  <div class="a btn-yellow" style="left:58px;top:143px;width:47px;height:12px">Sign Up today!</div>

  <div class="a service-zone" style="left:0;top:236px;width:481px;height:292px"></div>
  <div class="a feature-band" style="left:47px;top:199px;width:364px;height:61px">
    <div class="feature"><i></i>Quality Workmanship</div>
    <div class="feature"><i></i>Clean &amp; Comfortable</div>
    <div class="feature"><i></i>Service to your door</div>
  </div>

  <h2 class="a h-blue center" style="left:0;top:281px;width:481px;font-size:9.5px">Our Service</h2>
  <p class="a tiny center" style="left:136px;top:302px;width:208px;color:#4b5563">Our modern laundry processing center is designed for the efficiency our commercial clients expect. Our trained staff handles routine processing and the tougher issues of commercial laundry to deliver consistent quality and value.</p>

  <div class="a svc-card" style="left:110px;top:348px"><svg viewBox="0 0 20 20" fill="none" stroke="#26437a" stroke-width="1"><rect x="3" y="4" width="14" height="3" rx="1"/><rect x="3" y="8.5" width="14" height="3" rx="1"/><rect x="3" y="13" width="14" height="3" rx="1"/></svg><div class="svc-name">Commercial<br>Service</div><div class="svc-more">Learn more</div></div>
  <div class="a svc-card" style="left:179px;top:348px"><svg viewBox="0 0 20 20" fill="none" stroke="#26437a" stroke-width="1"><rect x="4" y="3" width="12" height="15" rx="1"/><circle cx="10" cy="11" r="4"/></svg><div class="svc-name">Light Commercial<br>Services</div><div class="svc-more">Learn more</div></div>
  <div class="a svc-card" style="left:248px;top:348px"><svg viewBox="0 0 20 20" fill="none" stroke="#26437a" stroke-width="1"><path d="M3 8 L10 3 L17 8 V17 H3 Z"/><path d="M7 17 V11 H13 V17"/></svg><div class="svc-name">Professional<br>Laundry Services</div><div class="svc-more">Learn more</div></div>
  <div class="a svc-card" style="left:317px;top:348px"><svg viewBox="0 0 20 20" fill="none" stroke="#26437a" stroke-width="1"><rect x="3" y="8" width="10" height="8" rx="1"/><path d="M13 10 H16 L18 13 V16 H13"/><circle cx="6" cy="17" r="1.5"/><circle cx="15" cy="17" r="1.5"/></svg><div class="svc-name">Pickup and<br>Delivery</div><div class="svc-more">Learn more</div></div>
  <div class="a svc-card" style="left:139px;top:426px"><svg viewBox="0 0 20 20" fill="none" stroke="#26437a" stroke-width="1"><path d="M6 3 L3 6 L5 8 V17 H15 V8 L17 6 L14 3 Q10 6 6 3 Z"/></svg><div class="svc-name">Wash Dry Fold</div><div class="svc-more">Learn more</div></div>
  <div class="a svc-card" style="left:208px;top:426px"><svg viewBox="0 0 20 20" fill="none" stroke="#26437a" stroke-width="1"><rect x="4" y="3" width="12" height="15" rx="1"/><circle cx="10" cy="11" r="3.5"/><path d="M4 6 H16"/></svg><div class="svc-name">Dry Cleaning</div><div class="svc-more">Learn more</div></div>
  <div class="a svc-card" style="left:277px;top:426px"><svg viewBox="0 0 20 20" fill="none" stroke="#26437a" stroke-width="1"><path d="M2 9 L10 4 L18 9"/><rect x="4" y="9" width="12" height="8"/><path d="M8 17 V12 H12 V17"/></svg><div class="svc-name">University Laundry<br>Program</div><div class="svc-more">Learn more</div></div>

  <div class="a photo" role="img" aria-label="Staff member holding folded white towels in front of washing machines" style="left:59px;top:567px;width:156px;height:126px;background:linear-gradient(135deg,#3f4752 0%,#9aa3ad 45%,#e8edf1 70%,#c9d2da 100%)"></div>
  <h2 class="a h-blue" style="left:252px;top:560px;font-size:9px">About Us</h2>
  <div class="a tiny" style="left:252px;top:580px;width:170px;color:#4b5563">
    <p style="margin-bottom:5px">Brightfold Laundry Company is a family-owned laundry service provider that has been serving Midtown Atlanta for over 45 years. We are proud to offer high quality and convenient services to local residents and business owners and strive to keep our customers' clothing in top shape.</p>
    <p style="margin-bottom:5px">Whether you have commercial laundry needs, are washing clothes for your family, or want to relax that weekend and have us pick up and wash/dry/fold for you, the professionals at Brightfold Laundry Company are ready to meet your goals. We provide express clothes and linen washing services to residential and commercial clients in Atlanta and surrounding areas.</p>
    <p>The pandemic has taught us the importance of our physical safety, so our pickup and delivery service ensures that you and your family remain safe. We have equipped our facility with Next Level Northvale laundry equipment, well trained and friendly employees to provide you the service you deserve. Brightfold also has a well maintained delivery van to pick up and deliver your laundry to your doorstep, giving you peace of mind.</p>
  </div>

  <div class="a setup-zone" style="left:0;top:734px;width:481px;height:221px"></div>
  <h2 class="a h-blue center" style="left:0;top:756px;width:481px;font-size:9.5px">Seeting up Service</h2>
  <p class="a center" style="left:0;top:778px;width:481px;font-size:5.3px;color:var(--ink)">Get Professional Laundry Cleaning Services For Your Clothes Without Any Hassle.</p>

  <div class="a step" style="left:87px;top:811px"><h4>Sign Up</h4><p>Give us a call at 404-555-0137 or use our sign up page to schedule service. You can control the frequency of how often we process your laundry.</p></div>
  <div class="a step-num" style="left:121px;top:803px">1</div>
  <div class="a step" style="left:201px;top:811px"><h4>Fill Out a<br>Customer Profile</h4><p>When setting up your customer profile you can detail how you want your laundry processed: hangers for shirts, pants folded, etc. You can select your laundry detergents, bleaches and softeners from a list of provided products.</p></div>
  <div class="a step-num" style="left:235px;top:803px">2</div>
  <div class="a step" style="left:315px;top:811px"><h4>Schedule a Pickup</h4><p>Place your clothes in the Brightfold Laundry Company bag and leave it out on your scheduled pickup day. We will process your clothing as instructed and deliver it back to your doorstep within 24 hours.</p></div>
  <div class="a step-num" style="left:349px;top:803px">3</div>
  <svg class="a" style="left:172px;top:842px" width="30" height="12" viewBox="0 0 30 12" fill="none" stroke="#26437a" stroke-width=".7" stroke-dasharray="1.5 1.5"><path d="M1 10 Q15 0 28 5"/><path d="M25 3 L28 5 L25 7" stroke-dasharray="none"/></svg>
  <svg class="a" style="left:286px;top:838px" width="30" height="12" viewBox="0 0 30 12" fill="none" stroke="#26437a" stroke-width=".7" stroke-dasharray="1.5 1.5"><path d="M1 3 Q15 1 28 8"/><path d="M25 6 L28 8 L25 10" stroke-dasharray="none"/></svg>

  <h2 class="a h-blue center" style="left:0;top:1005px;width:481px;font-size:9.5px">Why Choose Brightfold Laundry Company</h2>

  <div class="a photo" role="img" aria-label="Woman holding stacked towels between rows of washers" style="left:72px;top:1038px;width:125px;height:78px;background:linear-gradient(90deg,#444b55,#a8b0ba 50%,#4a515b)"></div>
  <div class="a why-text" style="left:213px;top:1039px"><h3 class="why-title">We Help You Optimize Your Time</h3><p class="tiny" style="color:#4b5563">Laundry is time consuming, especially for multi-tasking entrepreneurs. Brightfold Laundry Company makes a simple promise: we will give you your time back to focus on your business. Our goal is to provide your business with a clean, dry, and properly folded product every single time.</p></div>
  <div class="a btn-yellow" style="left:213px;top:1094px;width:46px;height:12px">Sign Up today!</div>

  <div class="a why-text" style="left:72px;top:1142px"><h3 class="why-title">We Have Knowledgeable, Friendly Team Members</h3><p class="tiny" style="color:#4b5563">Brightfold Laundry Company pairs friendly customer service with state-of-the-art equipment. We offer the cleanest facility in town, helpful attendants and equipment to handle all your laundering needs.</p></div>
  <div class="a photo" role="img" aria-label="Attendant with laundry cart in a bright laundromat" style="left:277px;top:1126px;width:125px;height:77px;background:linear-gradient(135deg,#c9d1d8,#f0f3f5 50%,#a9b2bb)"></div>

  <div class="a photo" role="img" aria-label="Smiling attendant holding folded towels beside a dryer" style="left:72px;top:1222px;width:125px;height:77px;background:linear-gradient(90deg,#5e656e,#d8dde1 55%,#b9c0c7)"></div>
  <div class="a why-text" style="left:217px;top:1232px"><h3 class="why-title">Our Facility is Bright, Clean and Comfortable</h3><p class="tiny" style="color:#4b5563">We keep the inside of our facilities well lit, clean and fully staffed. Our Next Level washers have advanced technology designed to get your order back to you within 24 hours.</p></div>

  <div class="a why-text" style="left:71px;top:1332px"><h3 class="why-title">We Utilize Modern, Industrial Size Washer and Dryer Equipment</h3><p class="tiny" style="color:#4b5563">Our technologically advanced machines can handle the biggest loads and oversized items like comforters that can be difficult to wash in the smaller machines. Our washers are designed to extract more water during the spin cycle and will reduce the dry time for you to finish your task quickly and affordably.</p></div>
  <div class="a photo" role="img" aria-label="Worker in red loading an industrial dryer" style="left:276px;top:1317px;width:125px;height:77px;background:linear-gradient(135deg,#3d4450,#8d96a1 45%,#b0475a 60%,#5b626c)"></div>

  <div class="a photo" role="img" aria-label="Hands holding a phone and a payment card" style="left:72px;top:1418px;width:125px;height:78px;background:linear-gradient(135deg,#f3ece6,#d9c2ae 50%,#c4a68c)"></div>
  <div class="a why-text" style="left:217px;top:1429px"><h3 class="why-title">We Provide Payment Options</h3><p class="tiny" style="color:#4b5563">Our payment platform provides you with payment choices. You can pay by credit card, laundry card or mobile app.</p></div>

  <div class="a why-text" style="left:72px;top:1525px"><h3 class="why-title">We Provide Customized Business Solutions</h3><p class="tiny" style="color:#4b5563">Schedule us to pick up your dirty clothes, and we will wash, dry and fold your laundry to your desired preferences. Keep your sanity and get more accomplished with help from the Brightfold Laundry Company team. This service is great for college students, busy parents, catering companies, party planners and business owners. We know every business has unique needs.</p></div>
  <div class="a photo" role="img" aria-label="Row of pressed shirts hanging on a rail" style="left:277px;top:1509px;width:125px;height:78px;background:linear-gradient(90deg,#3b4d6d,#9fb4cc 40%,#e7ecf1 60%,#43577a)"></div>

  <div class="a photo" role="img" aria-label="Shopping plaza storefront under a blue sky" style="left:71px;top:1605px;width:125px;height:77px;background:linear-gradient(180deg,#6fa7d8 0%,#b9d7ef 45%,#a88a5e 60%,#6e6a62 100%)"></div>
  <div class="a why-text" style="left:216px;top:1616px"><h3 class="why-title">Convenient Location</h3><p class="tiny" style="color:#4b5563">Located only half mile from Larkspur Plaza, Brightfold Laundry is close to your favorite shops and restaurants. If you are dropping off a rush order, you can run a few errands, do a little shopping or enjoy a mouthwatering BBQ at Copperpot Grill.</p></div>

  <h2 class="a cta-title" style="left:0;top:1747px;width:481px">Fast, Reliable, Affordable and<br>Professional Laundry For Clothes</h2>
  <div class="a btn-yellow" style="left:229px;top:1793px;width:47px;height:13px">Sign Up today!</div>
  <span class="chev" style="left:403px;top:1808px"></span>

  <h2 class="a h-blue" style="left:238px;top:1881px;font-size:9.5px">What to Expect</h2>
  <div class="a photo" role="img" aria-label="Housekeeper in grey uniform holding folded white towels" style="left:33px;top:1906px;width:175px;height:155px;background:linear-gradient(90deg,#fff 0%,#f1f1f1 25%,#d6d2cd 60%,#ece7e1 100%)"></div>
  <div class="a faq" style="left:241px;top:1903px">
    <div class="faq-item">Can I Customize My Service?</div>
    <div class="faq-open">When you call to sign up, we will help build out your laundry profile so we know how you want your laundry processed. You are in control of:<br>• Frequency of Service<br>• Choice of Soaps, Softeners, Bleach and Dryer Sheets<br>• Choice of water temperature<br>• Choice of dryer temperature<br>• Folded versus Hangers<br>• Special Instructions</div>
    <div class="faq-item" style="padding-top:7px">Are Laundry Bags Provided?</div>
    <div class="faq-item" style="padding-top:8px">What is the Turnaround Time?</div>
    <div class="faq-item" style="padding-top:8px">How Do We Pay?</div>
    <div class="faq-item" style="padding-top:8px">Do you have a referral program?</div>
    <div class="faq-item" style="padding-top:8px">Are you open on the Holidays?</div>
  </div>
  <span class="chev" style="left:403px;top:1902px"></span>
  <span class="chev" style="left:403px;top:1924px"></span>
  <span class="chev" style="left:403px;top:1944px"></span>
  <span class="chev" style="left:403px;top:1966px"></span>
  <span class="chev" style="left:403px;top:1986px"></span>

  <footer class="footer" style="height:121px;width:479px">
    <div class="f-col" style="left:64px;top:15px"><h5>Our Services</h5><ul><li>Commercial Services</li><li>Light Commercial Services</li><li>Professional Laundry Services</li><li>Pickup and Delivery</li><li>Wash Dry Fold</li><li>Dry Cleaning</li><li>University Laundry Program</li></ul></div>
    <div class="f-col" style="left:185px;top:16px"><h5>Quick Links</h5><ul><li>Our Services</li><li>Privacy Policy</li><li>Terms And Conditions</li><li>Blog</li><li>Wash Dry Fold</li><li>Dry Cleaning</li><li>University Laundry Program</li></ul></div>
    <div class="f-col" style="left:314px;top:22px">
      <div class="f-phone"><svg width="9" height="9" viewBox="0 0 24 24" fill="none" stroke="#fff" stroke-width="2"><path d="M5 3h4l2 5-3 2a12 12 0 0 0 6 6l2-3 5 2v4a2 2 0 0 1-2 2A17 17 0 0 1 3 5a2 2 0 0 1 2-2z"/></svg>555 0142 786</div>
      <p class="f-small">Lorem ipsum dolor sit amet,<br>consectetur adipiscing elit.</p>
      <div class="f-social"><i></i><i></i></div>
      <p class="f-small">© 2022 All Rights Reserved. Brightfold Laundry</p>
    </div>
  </footer>
</section>

<!-- ================= SERVICE DETAIL ================= -->
<h2 class="page-label" style="left:648px;top:222px">Page : Service detail</h2>
<section class="page" style="left:647px;top:284px;width:486px;height:907px">
  <div class="a detail-hero" style="left:0;top:32px;width:486px;height:216px"></div>
  <div class="a logo" style="left:56px;top:12px"><span class="logo-dot"></span>Brightfold Laundry</div>
  <nav class="a nav" style="left:183px;top:12px"><span class="on">Home</span><span>Services</span><span>Contact</span><span>Blog</span></nav>
  <div class="a social" style="left:350px;top:12px"><i></i><i></i></div>
  <div class="a btn-navy" style="left:380px;top:8px;width:47px;height:14px">Sign Up today!</div>

  <h1 class="a" style="left:67px;top:76px;font-size:14px;line-height:16px;font-weight:600;color:var(--ink)">Commercial<br>Services</h1>
  <p class="a tiny" style="left:67px;top:127px;width:158px;font-size:4.2px;line-height:7px;color:var(--ink)">Our state-of-the-art laundry processing center is designed for the efficiency our commercial clients expect. Our trained staff handles routine processing and the difficult issues of commercial laundry to deliver consistent quality and value.</p>
  <div class="a photo" role="img" aria-label="Mother and child loading front-loading washing machines" style="left:267px;top:71px;width:156px;height:123px;background:linear-gradient(90deg,#6b5a4c,#cdbfb2 40%,#f2ede8 65%,#b5aaa0)"></div>

  <h2 class="a center" style="left:0;top:280px;width:496px;font-size:9.5px;font-weight:600;color:var(--navy)">What We Launder</h2>
  <ul class="a launder-list" style="left:78px;top:307px"><li>Customer-Owned Goods such as:</li><li>Linens</li><li>Sheets</li><li>Pillow Cases</li><li>Table Cloths</li><li>Etc.</li></ul>
  <ul class="a launder-list" style="left:202px;top:307px"><li>Towels</li><li>Comforters and Bedspreads</li><li>Blankets and Pillows</li><li>Duvet Covers</li><li>Mattress Covers</li></ul>
  <ul class="a launder-list" style="left:321px;top:307px"><li>Uniforms</li><li>Scrubs</li><li>Reusable PPE</li><li>Curtains and Drapes</li></ul>

  <h2 class="a h-blue" style="left:254px;top:417px;font-size:9.5px">What to Expect</h2>
  <div class="a photo" role="img" aria-label="Housekeeper in grey uniform holding folded white towels" style="left:48px;top:441px;width:176px;height:157px;background:linear-gradient(90deg,#fff 0%,#f1f1f1 25%,#d6d2cd 60%,#ece7e1 100%)"></div>
  <div class="a faq" style="left:257px;top:440px">
    <div class="faq-item">Can I Customize My Service?</div>
    <div class="faq-open">When you call to sign up, we will help build out your laundry profile so we know how you want your laundry processed. You are in control of:<br>• Frequency of Service<br>• Choice of Soaps, Softeners, Bleach and Dryer Sheets<br>• Choice of water temperature<br>• Choice of dryer temperature<br>• Folded versus Hangers<br>• Special Instructions</div>
    <div class="faq-item" style="padding-top:7px">Are Laundry Bags Provided?</div>
    <div class="faq-item" style="padding-top:8px">What is the Turnaround Time?</div>
    <div class="faq-item" style="padding-top:8px">How Do We Pay?</div>
    <div class="faq-item" style="padding-top:8px">Do you have a referral program?</div>
    <div class="faq-item" style="padding-top:8px">Are you open on the Holidays?</div>
  </div>
  <span class="chev" style="left:421px;top:437px"></span>
  <span class="chev" style="left:421px;top:459px"></span>
  <span class="chev" style="left:421px;top:480px"></span>
  <span class="chev" style="left:421px;top:502px"></span>
  <span class="chev" style="left:421px;top:522px"></span>

  <h2 class="a cta-title" style="left:0;top:688px;width:486px">Fast, Reliable, Affordable and<br>Professional Laundry For Clothes</h2>
  <div class="a btn-yellow" style="left:223px;top:736px;width:47px;height:13px">Sign Up today!</div>

  <footer class="footer" style="height:122px">
    <div class="f-col" style="left:67px;top:15px"><h5>Our Services</h5><ul><li>Commercial Services</li><li>Light Commercial Services</li><li>Professional Laundry Services</li><li>Pickup and Delivery</li><li>Wash Dry Fold</li><li>Dry Cleaning</li><li>University Laundry Program</li></ul></div>
    <div class="f-col" style="left:189px;top:16px"><h5>Quick Links</h5><ul><li>Our Services</li><li>Privacy Policy</li><li>Terms And Conditions</li><li>Blog</li><li>Wash Dry Fold</li><li>Dry Cleaning</li><li>University Laundry Program</li></ul></div>
    <div class="f-col" style="left:319px;top:22px">
      <div class="f-phone"><svg width="9" height="9" viewBox="0 0 24 24" fill="none" stroke="#fff" stroke-width="2"><path d="M5 3h4l2 5-3 2a12 12 0 0 0 6 6l2-3 5 2v4a2 2 0 0 1-2 2A17 17 0 0 1 3 5a2 2 0 0 1 2-2z"/></svg>555 0142 786</div>
      <p class="f-small">Lorem ipsum dolor sit amet,<br>consectetur adipiscing elit.</p>
      <div class="f-social"><i></i><i></i></div>
      <p class="f-small">© 2022 All Rights Reserved. Brightfold Laundry</p>
    </div>
  </footer>
</section>

<!-- ================= FORM ENQUIRY ================= -->
<h2 class="page-label" style="left:654px;top:1227px">Page : Form enquiry</h2>
<section class="page" style="left:651px;top:1285px;width:482px;height:508px">
  <div class="a photo" role="img" aria-label="Housekeeper in grey uniform with towels in a bright room" style="left:200px;top:32px;width:282px;height:125px;background:linear-gradient(90deg,#fff 0%,#eeeeec 20%,#d8d3cd 55%,#efebe6 85%,#fff 100%)"></div>
  <div class="a logo" style="left:57px;top:12px"><span class="logo-dot"></span>Brightfold Laundry</div>
  <nav class="a nav" style="left:182px;top:12px"><span class="on">Home</span><span>Services</span><span>Contact</span><span>Blog</span></nav>
  <div class="a social" style="left:347px;top:12px"><i></i><i></i></div>
  <div class="a btn-navy" style="left:376px;top:8px;width:48px;height:14px">Sign Up today!</div>

  <h1 class="a" style="left:60px;top:63px;font-size:13px;line-height:16px;font-weight:600;color:var(--ink)">Fast, Reliable,<br>Affordable and<br>Professional Laundry<br>For Clothes</h1>

  <svg class="a" style="left:209px;top:210px" width="110" height="2"><line x1="0" y1="1" x2="110" y2="1" stroke="#CADEEF" stroke-width="1"/></svg>
  <div class="stepper-dot on" style="left:203px;top:204px">1</div>
  <div class="stepper-dot" style="left:252px;top:204px">2</div>
  <div class="stepper-dot" style="left:302px;top:204px">3</div>

  <label class="a" style="left:128px;top:242px;font-size:5.5px;font-weight:700;color:var(--ink)">What service do you provide?*</label>
  <div class="a select-box" style="left:128px;top:256px;width:263px;height:62px">
    <div class="select-field">What service do you provide?<span class="chev" style="right:8px;top:3px"></span></div>
    <div class="select-opt" style="padding-top:6px">Short-term Rental (StayNook/Rentwell/Other)</div>
    <div class="select-opt">Wellness (Massage Therapy, Cryotherapy, Fitness, etc.)</div>
    <div class="select-opt">Other</div>
  </div>
  <div class="a btn-navy" style="left:354px;top:339px;width:37px;height:13px">Next</div>

  <footer class="footer" style="height:123px">
    <div class="f-col" style="left:66px;top:15px"><h5>Our Services</h5><ul><li>Commercial Services</li><li>Light Commercial Services</li><li>Professional Laundry Services</li><li>Pickup and Delivery</li><li>Wash Dry Fold</li><li>Dry Cleaning</li><li>University Laundry Program</li></ul></div>
    <div class="f-col" style="left:187px;top:16px"><h5>Quick Links</h5><ul><li>Our Services</li><li>Privacy Policy</li><li>Terms And Conditions</li><li>Blog</li><li>Wash Dry Fold</li><li>Dry Cleaning</li><li>University Laundry Program</li></ul></div>
    <div class="f-col" style="left:316px;top:22px">
      <div class="f-phone"><svg width="9" height="9" viewBox="0 0 24 24" fill="none" stroke="#fff" stroke-width="2"><path d="M5 3h4l2 5-3 2a12 12 0 0 0 6 6l2-3 5 2v4a2 2 0 0 1-2 2A17 17 0 0 1 3 5a2 2 0 0 1 2-2z"/></svg>555 0142 786</div>
      <p class="f-small">Lorem ipsum dolor sit amet,<br>consectetur adipiscing elit.</p>
      <div class="f-social"><i></i><i></i></div>
      <p class="f-small">© 2022 All Rights Reserved. Brightfold Laundry</p>
    </div>
  </footer>
</section>

</div>
</body>
</html>
```